Small corporate website template design

I need a couple templates designed for a small corporate website. The corporate site reflects the existence of the parent company which will own various brands/services that have their own websites, so it will mainly be used to present who we are, what we do, what is happening (news/events), how to contact us, link off to our other brand/service sites, as well as post information for public relations, investors, and job opportunities.

The company name is Vornelight LLC (www.vornelight.example), and the name is representative of stratified layers of interconnected digital services. The corporate site is not expected to generate a bunch of fanfare - that honor will be reserved for the externally linked brand/service sites.

The provided logo may be manipulated in color, size, shape, positioning, etc. to get it to fit with the design, but should be integrated in some way.

What we are looking for is a home page layout as well as a template for an inner page whereby the navigation/logo, etc may be diminished to some extent for the inner pages. We are also interested in reusable elements such as dividers, content containers, etc. in order to represent the types of information described above that we would like to present as described above.

We are particularly interested in consistency of design elements, conservative use of color (including consideration of accessibility concerns), judicious use of whitespace in favor of simplified messaging, and something lending itself well to internationalization/translation.

Target Market(s)

Small business owners, entrepreneurs (B2B)

Number of Pages Required

2 page

Font styles to use
Sans Serif

Requirements
Must have
• See the attached PDF with the logo concept, color swatches, and comparative sites.

```html
<!DOCTYPE html>
<html lang="en">
<head>
<meta charset="utf-8">
<title>Vornelight LLC</title>
<link rel="stylesheet" href="https://fonts.googleapis.com/css2?family=Raleway:wght@400;500;600;700;800&display=swap">
<style>
:root{
  --navy:#0d3168;
  --navy-deep:#0a2755;
  --orange:#d0680f;
  --orange-soft:#e08a3a;
  --ice:#eef5fc;
  --grey-band:#efefef;
  --ink:#444a55;
  --white:#ffffff;
}
*{margin:0;padding:0;box-sizing:border-box}
html,body{width:1200px;height:3673px;overflow:hidden}
body{position:relative;background:var(--white);font-family:"Raleway",Arial,sans-serif;color:var(--ink)}
.abs{position:absolute}
.center{text-align:center}

/* hero */
.hero{left:0;top:0;width:1200px;height:640px}
.hero-bg{position:absolute;inset:0;background:linear-gradient(120deg,#c86e1c 0%,#e0964e 45%,#d07a2c 75%,#b7651d 100%)}
.hero-curve{position:absolute;left:0;top:0}
.brand{left:70px;top:26px;display:flex;align-items:center;gap:12px;font-weight:700;font-size:28px;color:var(--navy)}
.brand-dot{width:26px;height:26px;border-radius:50%;background:var(--navy)}
.nav{left:578px;top:41px;display:flex;gap:26px;font-size:14px;font-weight:500;color:var(--white);letter-spacing:.3px}
.nav .active{color:var(--navy);font-weight:600}
.btn-login{left:1009px;top:27px;width:113px;height:46px;border:2px solid var(--white);border-radius:23px;background:var(--orange);color:var(--white);font-weight:600;font-size:18px;line-height:42px;text-align:center}
.hero-title{left:0;top:150px;width:1200px;font-size:41px;font-weight:600;line-height:52px;color:var(--white)}
.hero-sub{left:0;top:264px;width:1200px;font-size:18px;font-weight:700;color:var(--navy)}
.device{left:282px;top:335px;width:636px;height:363px}
.device-screen{position:absolute;left:60px;top:0;width:516px;height:340px;border-radius:14px;background:#1b1b1f;padding:14px}
.device-view{width:100%;height:100%;background:radial-gradient(circle at 45% 45%,#bfe6ff 0%,#3e7fb2 25%,#13355e 60%,#0a1a33 100%)}
.device-base{position:absolute;left:0;top:340px;width:636px;height:20px;border-radius:0 0 40px 40px;background:linear-gradient(#e6e6e6,#a9a9a9)}

/* headings */
.section-title{font-size:44px;font-weight:700;color:var(--navy);letter-spacing:1px}
.section-kicker{font-size:18px;font-weight:500;color:var(--orange)}
.body-copy{font-size:14px;line-height:30px;color:var(--ink)}
.btn{height:50px;border-radius:25px;background:var(--orange);color:var(--white);font-size:19px;font-weight:500;line-height:50px;text-align:center}

/* services */
.services{left:0;top:1134px;width:1200px;height:397px;background:var(--navy)}
.services-intro{position:absolute;left:0;top:0;width:416px;height:397px;background:var(--ice)}
.services-title{left:78px;top:1262px;font-size:44px;font-weight:700;line-height:52px;color:var(--navy)}
.services-kicker{left:80px;top:1376px}
.hex{width:225px;height:260px}
.hex-label{position:absolute;left:0;top:150px;width:225px;text-align:center;font-size:18px;font-weight:700;line-height:24px;color:var(--navy)}
.hex-icon{position:absolute;left:72px;top:50px}

/* why */
.person{left:965px;top:1616px;width:235px;height:384px;background:linear-gradient(180deg,#f4f4f4 0%,#e7ddd3 60%,#f2f2f2 100%);z-index:0}
.why-layer{z-index:1}
.tab{height:49px;border:1.5px solid #9aa0a8;border-radius:25px;background:var(--white);font-size:16px;line-height:46px;text-align:center;color:var(--ink);white-space:nowrap}
.tab.is-active{background:var(--navy);border-color:var(--navy);color:var(--white)}

/* testimonial */
.testimonial{left:0;top:2003px;width:1200px;height:184px;background:var(--grey-band)}
.quote-badge{left:159px;top:2042px;width:110px;height:110px;border:3px solid var(--orange);border-radius:50%;font-size:48px;font-weight:800;color:var(--orange);line-height:110px;text-align:left;padding-left:20px}
.avatar{left:218px;top:2042px;width:106px;height:106px;border-radius:50%;border:3px solid var(--navy);background:linear-gradient(135deg,#e9e4df,#c8b59d)}
.quote-text{left:358px;top:2056px;width:620px}
.client-name{left:942px;top:2132px;font-size:16px;font-weight:700;color:var(--navy)}
.client-name::before{content:"";display:inline-block;width:24px;height:3px;background:var(--navy);vertical-align:middle;margin-right:12px}

/* news */
.news-photo{left:140px;top:2349px;width:448px;height:291px;background:linear-gradient(120deg,#3c4250 0%,#8e939b 45%,#d9dde2 100%)}
.news-date{font-size:15px;color:var(--ink);display:flex;align-items:center;gap:10px}
.news-feature-title{left:620px;top:2436px;width:440px;font-size:19px;font-weight:700;line-height:30px;color:var(--navy)}
.read-more{left:620px;top:2598px;font-size:18px;color:var(--orange);display:flex;align-items:center;gap:12px}
.card{top:2682px;height:208px}
.card-bg{position:absolute;inset:0}
.card-plain .card-bg{background:linear-gradient(120deg,#e7e9ec,#f6f6f6 60%,#dcdfe3)}
.card-accent .card-bg{background:linear-gradient(120deg,#c9620c,#d67f2f 60%,#b85a10)}
.card-date{position:absolute;left:24px;top:44px}
.card-title{position:absolute;left:24px;top:90px;width:245px;font-size:16px;font-weight:700;line-height:26px;color:var(--navy-deep)}
.card-accent .card-title,.card-accent .card-date{color:var(--white)}
.card-arrow{position:absolute;right:18px;bottom:28px}

/* contact */
.contact-band{left:0;top:3029px;width:1200px;height:461px;background:linear-gradient(160deg,#2a5688 0%,#1a4980 50%,#123c7a 100%)}
.contact-info{left:644px;top:2946px;width:426px;height:417px;background:var(--orange);padding:48px 0 0 70px;color:var(--navy)}
.contact-info h2{font-size:30px;font-weight:700;letter-spacing:.5px;margin-bottom:26px}
.info-row{display:flex;gap:20px;font-size:14px;line-height:24px;margin-bottom:22px;color:var(--white)}
.info-row .label{color:var(--navy);font-weight:600}
.info-icon{width:20px;flex:none;margin-top:3px}
.socials{display:flex;gap:12px;margin-top:10px}
.social{width:46px;height:46px;border-radius:50%;background:var(--navy)}
.form-frame{left:174px;top:3110px;width:499px;height:466px;border:1px solid rgba(255,255,255,.55);padding:40px 0 0 34px}
.form-frame h2{font-size:36px;font-weight:600;color:var(--white);letter-spacing:1px}
.form-note{font-size:13px;color:var(--orange-soft);margin:8px 0 22px}
.field{width:290px;border-bottom:1px solid rgba(255,255,255,.5);font-size:13px;color:rgba(255,255,255,.75);padding-bottom:10px;margin-bottom:30px}
.field.tall{height:80px}
.btn-submit{left:220px;top:3507px;width:145px;height:51px}
.footer-note{left:0;top:3614px;width:1200px;font-size:14px;color:var(--ink)}
.footer-note b{color:var(--navy)}
.footer-bar{left:0;top:3661px;width:1200px;height:12px;background:var(--navy)}
</style>
</head>
<body>

<header class="abs hero">
  <div class="hero-bg" role="img" aria-label="Team working at a desk with laptops, warm orange tint"></div>
  <svg class="hero-curve" width="1200" height="640" viewBox="0 0 1200 640" aria-hidden="true">
    <path d="M0 580 Q600 500 1200 580 L1200 640 L0 640 Z" fill="#ffffff"/>
  </svg>
</header>
<div class="abs brand"><span class="brand-dot"></span>Vornelight</div>
<nav class="abs nav"><span class="active">HOME</span><span>ABOUT</span><span>SERVICES</span><span>NEWS</span><span>CONTACT</span></nav>
<div class="abs btn-login">LOGIN</div>
<h1 class="abs hero-title center">Adaptive Software Technology for the<br>Digital Revolution</h1>
<p class="abs hero-sub center">Digital Layers To Raise The Quality Of Life</p>
<div class="abs device">
  <div class="device-screen"><div class="device-view" role="img" aria-label="Laptop screen showing a glowing network of connected digital icons above a hand"></div></div>
  <div class="device-base"></div>
</div>

<h2 class="abs section-title center" style="left:0;top:752px;width:1200px">WELCOME TO VORNELIGHT</h2>
<p class="abs section-kicker center" style="left:0;top:808px;width:1200px">Who We Are</p>
<div class="abs body-copy center" style="left:200px;top:846px;width:800px">
  <p>Lorem Ipsum is simply dummy text of the printing and typesetting industry. Lorem Ipsum has been the industry's standard dummy text ever since the 1500s, when an unknown printer took a galley of type and scrambled it to make a type specimen book. It has survived not only five centuries.</p>
  <p style="margin-top:8px">Lorem Ipsum is simply dummy text of the printing and typesetting industry. Lorem Ipsum has been the industry's standard dummy text ever since the 1500s, when an unknown printer took a galley</p>
</div>
<div class="abs btn" style="left:507px;top:1011px;width:186px">LEARN MORE</div>

<section class="abs services"><div class="services-intro"></div></section>
<h2 class="abs services-title">OUR<br>SERVICES</h2>
<p class="abs section-kicker services-kicker">What We Do</p>

<div class="abs hex" style="left:358px;top:1224px">
  <svg width="225" height="260" viewBox="0 0 225 260" aria-hidden="true"><polygon points="112.5,0 225,65 225,195 112.5,260 0,195 0,65" fill="#fff"/></svg>
  <svg class="hex-icon" width="80" height="80" viewBox="0 0 80 80" fill="none" stroke="#d0680f" stroke-width="2.5" aria-hidden="true">
    <rect x="8" y="8" width="64" height="44"/><line x1="40" y1="52" x2="40" y2="74"/><line x1="40" y1="52" x2="22" y2="76"/><line x1="40" y1="52" x2="58" y2="76"/>
    <circle cx="24" cy="28" r="9"/><path d="M38 40 L50 26 L62 36"/><line x1="44" y1="16" x2="52" y2="22"/>
  </svg>
  <div class="hex-label">MARKETING<br>STRATEGY</div>
</div>
<div class="abs hex" style="left:630px;top:1224px">
  <svg width="225" height="260" viewBox="0 0 225 260" aria-hidden="true"><polygon points="112.5,0 225,65 225,195 112.5,260 0,195 0,65" fill="#fff"/></svg>
  <svg class="hex-icon" width="80" height="80" viewBox="0 0 80 80" fill="none" stroke="#d0680f" stroke-width="2.5" aria-hidden="true">
    <rect x="10" y="16" width="10" height="56"/><rect x="28" y="40" width="10" height="32"/><rect x="46" y="30" width="10" height="42"/><rect x="62" y="54" width="10" height="18"/><line x1="4" y1="74" x2="78" y2="74"/>
  </svg>
  <div class="hex-label">DIGITAL<br>ANALYTICS</div>
</div>
<div class="abs hex" style="left:897px;top:1224px">
  <svg width="225" height="260" viewBox="0 0 225 260" aria-hidden="true"><polygon points="112.5,0 225,65 225,195 112.5,260 0,195 0,65" fill="#fff"/></svg>
  <svg class="hex-icon" width="80" height="80" viewBox="0 0 80 80" fill="none" stroke="#d0680f" stroke-width="2.5" aria-hidden="true">
    <path d="M6 14 H30 L36 22 H74 V70 H6 Z"/><line x1="6" y1="30" x2="74" y2="30"/>
    <circle cx="24" cy="52" r="5"/><circle cx="40" cy="44" r="5"/><circle cx="56" cy="52" r="5"/><path d="M28 50 L36 46 M44 46 L52 50"/>
  </svg>
  <div class="hex-label">MANAGEMENT &amp;<br>OPTIMIZATION</div>
</div>

<div class="abs person" role="img" aria-label="Smiling young man in a white t-shirt holding a tablet"></div>
<h2 class="abs section-title center why-layer" style="left:0;top:1588px;width:1200px">WHY VORNELIGHT ?</h2>
<p class="abs section-kicker center why-layer" style="left:0;top:1641px;width:1200px">What We offer</p>
<div class="abs tab is-active why-layer" style="left:289px;top:1695px;width:196px">PUBLIC RELATIONS</div>
<div class="abs tab why-layer" style="left:497px;top:1695px;width:196px">INVESTORS</div>
<div class="abs tab why-layer" style="left:703px;top:1695px;width:208px">JOB OPPORTUNITIES</div>
<p class="abs body-copy center why-layer" style="left:305px;top:1770px;width:590px">Lorem Ipsum is simply dummy text of the printing and typesetting industry. Lorem Ipsum has been the industry's standard dummy text ever since the 1500s, when an unknown printer took a galley</p>
<div class="abs btn why-layer" style="left:507px;top:1878px;width:186px">LEARN MORE</div>

<section class="abs testimonial"></section>
<svg class="abs" style="left:76px;top:2070px" width="20" height="46" viewBox="0 0 20 46" aria-hidden="true"><path d="M18 2 L3 23 L18 44" fill="none" stroke="#8b8f96" stroke-width="2"/></svg>
<svg class="abs" style="left:1104px;top:2070px" width="20" height="46" viewBox="0 0 20 46" aria-hidden="true"><path d="M2 2 L17 23 L2 44" fill="none" stroke="#8b8f96" stroke-width="2"/></svg>
<div class="abs quote-badge">“</div>
<div class="abs avatar" role="img" aria-label="Portrait of the client"></div>
<p class="abs body-copy quote-text">" Lorem Ipsum is simply dummy text of the printing and typesetting industry. Lorem Ipsum has been the industry's standard dummy text ever since the 1500s, when an unknown printer took a galley "</p>
<div class="abs client-name">Client Name</div>

<h2 class="abs section-title center" style="left:0;top:2248px;width:1200px">NEWS/EVENTS</h2>
<p class="abs section-kicker center" style="left:0;top:2302px;width:1200px">Who We Are</p>
<div class="abs news-photo" role="img" aria-label="Two businessmen in suits working at a laptop"></div>
<div class="abs news-date" style="left:622px;top:2378px">
  <svg width="16" height="16" viewBox="0 0 16 16" aria-hidden="true"><rect x="1" y="3" width="14" height="12" fill="none" stroke="#444a55" stroke-width="1.6"/><line x1="1" y1="7" x2="15" y2="7" stroke="#444a55" stroke-width="1.6"/><line x1="5" y1="1" x2="5" y2="5" stroke="#444a55" stroke-width="1.6"/><line x1="11" y1="1" x2="11" y2="5" stroke="#444a55" stroke-width="1.6"/></svg>19 May 2018
</div>
<div class="abs" style="left:622px;top:2410px;width:110px;height:2px;background:#444a55"></div>
<h3 class="abs news-feature-title">Lorem Ipsum is simply dummy text of the printing typesetting industry.</h3>
<p class="abs body-copy" style="left:620px;top:2500px;width:440px;font-size:13px;line-height:28px">Lorem Ipsum is simply dummy text of the printing and typesetting industry. Lorem Ipsum has been the industry.</p>
<div class="abs read-more"><svg width="36" height="14" viewBox="0 0 36 14" aria-hidden="true"><path d="M0 7 H32 M26 1 L33 7 L26 13" fill="none" stroke="#d0680f" stroke-width="2.5"/></svg>Read More</div>

<article class="abs card card-plain" style="left:140px;width:289px">
  <div class="card-bg" role="img" aria-label="Office team photo, faded"></div>
  <div class="news-date card-date"><svg width="14" height="14" viewBox="0 0 16 16" aria-hidden="true"><rect x="1" y="3" width="14" height="12" fill="none" stroke="#d0680f" stroke-width="1.8"/><line x1="1" y1="7" x2="15" y2="7" stroke="#d0680f" stroke-width="1.8"/></svg>19 May 2018</div>
  <h4 class="card-title">Lorem Ipsum is simply text of the printing type.</h4>
  <svg class="card-arrow" width="36" height="14" viewBox="0 0 36 14" aria-hidden="true"><path d="M0 7 H32 M26 1 L33 7 L26 13" fill="none" stroke="#d0680f" stroke-width="2.5"/></svg>
</article>
<article class="abs card card-accent" style="left:453px;width:294px">
  <div class="card-bg" role="img" aria-label="Meeting room photo with orange overlay"></div>
  <div class="news-date card-date"><svg width="14" height="14" viewBox="0 0 16 16" aria-hidden="true"><rect x="1" y="3" width="14" height="12" fill="none" stroke="#ffffff" stroke-width="1.8"/><line x1="1" y1="7" x2="15" y2="7" stroke="#ffffff" stroke-width="1.8"/></svg>19 May 2018</div>
  <h4 class="card-title">Lorem Ipsum is simply text of the printing type.</h4>
  <svg class="card-arrow" width="36" height="14" viewBox="0 0 36 14" aria-hidden="true"><path d="M0 7 H32 M26 1 L33 7 L26 13" fill="none" stroke="#ffffff" stroke-width="2.5"/></svg>
</article>
<article class="abs card card-plain" style="left:771px;width:292px">
  <div class="card-bg" role="img" aria-label="Colleague at a laptop, faded"></div>
  <div class="news-date card-date"><svg width="14" height="14" viewBox="0 0 16 16" aria-hidden="true"><rect x="1" y="3" width="14" height="12" fill="none" stroke="#d0680f" stroke-width="1.8"/><line x1="1" y1="7" x2="15" y2="7" stroke="#d0680f" stroke-width="1.8"/></svg>19 May 2018</div>
  <h4 class="card-title">Lorem Ipsum is simply text of the printing type.</h4>
  <svg class="card-arrow" width="36" height="14" viewBox="0 0 36 14" aria-hidden="true"><path d="M0 7 H32 M26 1 L33 7 L26 13" fill="none" stroke="#d0680f" stroke-width="2.5"/></svg>
</article>

<section class="abs contact-band"></section>
<div class="abs contact-info">
  <h2>CONTACT INFO</h2>
  <div class="info-row">
    <svg class="info-icon" viewBox="0 0 20 26" height="26" aria-hidden="true"><path d="M10 1 C4 1 1 5 1 10 C1 17 10 25 10 25 C10 25 19 17 19 10 C19 5 16 1 10 1 Z" fill="#0d3168"/><circle cx="10" cy="10" r="3.5" fill="#d0680f"/></svg>
    <div><div class="label">VORNELIGHT</div>101 - lorem ipsum is simple<br>dummy text of print.</div>
  </div>
  <div class="info-row">
    <svg class="info-icon" viewBox="0 0 20 16" height="16" aria-hidden="true"><rect x="0" y="1" width="20" height="14" fill="#0d3168"/><path d="M0 2 L10 9 L20 2" fill="none" stroke="#d0680f" stroke-width="1.5"/></svg>
    <div>info@vornelight.example</div>
  </div>
  <div class="info-row">
    <svg class="info-icon" viewBox="0 0 20 20" height="20" aria-hidden="true"><path d="M4 1 L8 5 L6 8 C7 11 9 13 12 14 L15 12 L19 16 L16 19 C8 18 2 12 1 4 Z" fill="#0d3168"/></svg>
    <div>123 456 7890</div>
  </div>
  <div class="socials">
    <span class="social" aria-label="Social profile one"></span>
    <span class="social" aria-label="Social profile two"></span>
    <span class="social" aria-label="Social profile three"></span>
  </div>
</div>

<form class="abs form-frame">
  <h2>CONTACT US</h2>
  <p class="form-note">Need An More Question Please Fill The Form</p>
  <div class="field">Name *</div>
  <div class="field">Email *</div>
  <div class="field">Phone *</div>
  <div class="field tall">Message *</div>
</form>
<div class="abs btn btn-submit">SUBMIT</div>

<p class="abs footer-note center">© <b>VORNELIGHT</b> - 2018 All Right Reserved.</p>
<div class="abs footer-bar"></div>

</body>
</html>
```